Harborline Energy - needs a business card

Harborline Energy is a U.S. based diesel sourcing and distribution company that supports American oil & gas fields through providing quality product and consistent services.

Target Market(s)

Oil and Gas

Contact Information for Business Card

The background of the card must be white to ensure the logo pops.

Font styles to use
Serif
Sans Serif

Colors

Designer to choose colors to be used in the design.

Requirements
Must have
• Front of Card: Tag line: Harborline Energy, Powering America's Oil & Gas fields.
• Not sure if you guys do this part but just in case...
• Dale Menschow
• Owner/CEO
• C:555.318.4076
• E:Dmenschow@harborlineenergy.example
• W:Harborlineenergy.example
• Locations: Servicing the Powder River, DJ basin and Bakken formations.
• Back of Card: " Frac fueling is what we do. We understand how important diesel fuel is to your operation, which is why our main service line is Frac fueling. We assure our supply and stand by our service"

```html
<!DOCTYPE html>
<html lang="en">
<head>
<meta charset="utf-8">
<title>Harborline Energy – Business Card</title>
<link href="https://fonts.googleapis.com/css2?family=Archivo:wght@400;800&family=Open+Sans:wght@400;700&display=swap" rel="stylesheet">
<style>
  :root {
    --navy: #062b5c;
    --red: #b5121b;
    --white: #ffffff;
    --backdrop: #d1d2d4;
    --edge: #b9babc;
  }
  * { margin: 0; padding: 0; box-sizing: border-box; }
  html, body { width: 1200px; height: 1052px; overflow: hidden; background: var(--backdrop); }
  .stage { position: relative; width: 1200px; height: 1052px; }

  .card {
    position: absolute;
    background: var(--white);
    border: 1px solid var(--edge);
    border-radius: 35px;
    overflow: hidden;
  }
  .card--front { left: 58px; top: 70px; width: 766px; height: 436px; }
  .card--back  { left: 395px; top: 550px; width: 764px; height: 437px; }

  .brand {
    position: absolute;
    display: flex; flex-direction: column; align-items: center;
  }
  .brand__dot { width: 120px; height: 120px; border-radius: 50%; background: var(--navy); }
  .brand__name {
    margin-top: 26px;
    font-family: "Archivo", sans-serif;
    font-weight: 800;
    font-size: 27px;
    letter-spacing: 1px;
    color: var(--navy);
    text-transform: uppercase;
    white-space: nowrap;
  }
  .card--front .brand { left: 40px; width: 330px; top: 95px; }
  .card--back .brand { left: 0; width: 764px; top: 55px; }

  .site-band {
    position: absolute; left: 407px; top: 59px; width: 36px; height: 310px;
    background: var(--red);
    display: flex; align-items: center; justify-content: center;
  }
  .site-band span {
    transform: rotate(-90deg);
    white-space: nowrap;
    font-family: "Open Sans", sans-serif;
    font-size: 14px; letter-spacing: 1.6px;
    color: var(--white);
  }

  .contact-panel {
    position: absolute; left: 446px; top: 59px; width: 320px; height: 310px;
    background: var(--navy); color: var(--white);
    padding: 24px 12px 0 14px;
    font-family: "Open Sans", sans-serif;
  }
  .contact-panel__name {
    font-family: "Archivo", sans-serif; font-weight: 800;
    font-size: 25px; letter-spacing: 1px; text-transform: uppercase;
  }
  .contact-panel__role {
    font-family: "Archivo", sans-serif; font-size: 19px; margin-top: 2px; letter-spacing: .5px;
  }
  .contact-panel__area { font-size: 17px; line-height: 28px; margin-top: 22px; }
  .contact-panel__list { list-style: none; margin-top: 18px; font-size: 14px; }
  .contact-panel__list li { display: flex; align-items: center; gap: 8px; height: 30px; white-space: nowrap; }
  .contact-panel__list svg { width: 14px; height: 14px; flex: none; }

  .tagline {
    position: absolute; left: 0; right: 0; top: 398px; text-align: center;
    font-family: "Archivo", sans-serif; font-size: 17px; letter-spacing: .8px;
    color: var(--navy); text-transform: uppercase;
  }

  .service {
    position: absolute; left: 0; right: 0; top: 323px; text-align: center;
    font-family: "Open Sans", sans-serif; color: #1a1a1a;
  }
  .service__title { font-weight: 700; font-size: 17px; color: var(--navy); margin-bottom: 4px; }
  .service__text { font-size: 16.5px; line-height: 26px; }
</style>
</head>
<body>
<main class="stage">

  <section class="card card--front">
    <div class="brand">
      <div class="brand__dot"></div>
      <div class="brand__name">Harborline Energy</div>
    </div>

    <div class="site-band"><span>www.harborlineenergy.example</span></div>

    <div class="contact-panel">
      <div class="contact-panel__name">Dale Menschow</div>
      <div class="contact-panel__role">OWNER/CEO</div>
      <p class="contact-panel__area">Servicing the Powder River<br>DJ basin and Bakken formations.</p>
      <ul class="contact-panel__list">
        <li>
          <svg viewBox="0 0 16 16" aria-hidden="true"><circle cx="8" cy="8" r="7" fill="none" stroke="#fff" stroke-width="1.2"/><path d="M5.5 4.5l1.5 1.5-1 1.2c.6 1.3 1.5 2.2 2.8 2.8l1.2-1 1.5 1.5-1.2 1.2c-2.6-.4-5-2.8-5.4-5.4z" fill="#fff"/></svg>
          555.318.4076
        </li>
        <li>
          <svg viewBox="0 0 16 16" aria-hidden="true"><rect x="1.5" y="4" width="13" height="9" rx="1" fill="#fff"/><path d="M1.5 4.5l6.5 5 6.5-5" fill="none" stroke="#062b5c" stroke-width="1.2"/></svg>
          dmenschow@harborlineenergy.example
        </li>
      </ul>
    </div>

    <p class="tagline">Harborline Energy, Powering America's Oil &amp; Gas fields.</p>
  </section>

  <section class="card card--back">
    <div class="brand">
      <div class="brand__dot"></div>
      <div class="brand__name">Harborline Energy</div>
    </div>
    <div class="service">
      <h2 class="service__title">Frac Fueling Is What We Do.</h2>
      <p class="service__text">We understand how important diesel fuel is to your operation which<br>is why our main service line is Frac fueling. We assure our supply and stand by our service</p>
    </div>
  </section>

</main>
</body>
</html>
```